Bref créative
Stationery - Business Card / Letterhead
For Public Adjusting Company
Professional
Doran T. Whitcombe
Sr. Public Adjuster
58 W. Alder St.
Suite 612
Smithtown, NY 11492
doran@trclaimpro.com
www.trclaimpro.com
On the front I want our logo with the shadow on the bottom
On the back I would like you to incorporate a little creative usage of either the shield/lighthouse logo and all of my information
This logo should be used as the front as it has the bottom shadow which for some reason is not showing up on the other logos
the business card front will be high gloss finish
Also the fax number should be 516.843.9075 not 829. there is no where else for me to edit that once the project is uploaded

```html
<!DOCTYPE html>
<html lang="en">
<head>
<meta charset="utf-8">
<title>TR Claim Advisors — Stationery</title>
<link href="https://fonts.googleapis.com/css2?family=Cinzel:wght@600&family=Open+Sans:wght@400;600&display=swap" rel="stylesheet">
<style>
  :root{
    --navy:#163a6b;
    --navy-deep:#0c2447;
    --navy-light:#2f5e99;
    --red:#c8232c;
    --paper:#ffffff;
    --paper-shade:#eef0f3;
    --ink:#3d4650;
    --muted:#8a939c;
    --backdrop:#e7e4df;
    --watermark:rgba(22,58,107,.06);
  }
  *{box-sizing:border-box;margin:0;padding:0}
  html,body{width:1200px;height:1002px;overflow:hidden}
  body{background:var(--backdrop);font-family:"Open Sans",Arial,sans-serif;color:var(--ink);position:relative}
  .sheet{position:absolute;background:var(--paper);box-shadow:0 2px 10px rgba(0,0,0,.12);overflow:hidden}

  .brand{display:flex;align-items:center;gap:10px;white-space:nowrap}
  .brand-mark{width:26px;height:26px;background:var(--navy);flex:none}
  .brand-name{font-family:"Cinzel",Georgia,serif;font-weight:600;color:var(--navy);font-size:19px;letter-spacing:1px;line-height:1}
  .brand.on-dark .brand-mark{background:#fff}
  .brand.on-dark .brand-name{color:#fff}

  .watermark{position:absolute;background:var(--watermark)}

  /* Envelope back, flap open */
  .envelope-back{position:absolute;left:60px;top:30px;width:500px;height:232px}
  .envelope-back .flap{position:absolute;left:0;top:0;width:500px;height:82px}
  .envelope-back .flap-site{position:absolute;left:0;right:0;top:30px;text-align:center;font-size:10px;letter-spacing:1.5px;color:rgba(255,255,255,.85)}
  .envelope-back .pocket{position:absolute;left:0;top:82px;width:500px;height:150px;background:var(--paper);box-shadow:0 2px 10px rgba(0,0,0,.12)}
  .envelope-back .pocket svg{position:absolute;inset:0}

  /* Envelope front */
  .envelope{left:60px;top:290px;width:500px;height:217px}
  .envelope .brand{position:absolute;left:26px;top:26px}
  .envelope .rule{position:absolute;left:26px;right:26px;top:62px;height:2px;background:linear-gradient(90deg,var(--navy) 0 70%,var(--red) 70%)}
  .envelope .return{position:absolute;left:26px;top:70px;font-size:9px;color:var(--muted)}
  .envelope .watermark{left:300px;top:90px;width:100px;height:100px}

  /* Business card back */
  .card-back{left:60px;top:542px;width:360px;height:206px}
  .card-back .brand{position:absolute;left:16px;top:16px;gap:8px}
  .card-back .brand-name{font-size:15px}
  .card-back .brand-mark{width:20px;height:20px}
  .card-back .rule{position:absolute;left:16px;right:16px;top:46px;height:2px;background:linear-gradient(90deg,var(--navy) 0 70%,var(--red) 70%)}
  .card-back .name-bar{position:absolute;right:0;top:58px;width:176px;background:var(--navy);color:#fff;padding:6px 12px;text-align:right}
  .card-back .person{font-weight:600;font-size:12px;white-space:nowrap}
  .card-back .title{font-size:8.5px;opacity:.85}
  .card-back .details{position:absolute;left:16px;top:60px;font-size:9px;line-height:1.5}
  .card-back .details .label{color:var(--navy);font-weight:600}
  .card-back .watermark{left:240px;top:106px;width:72px;height:72px}
  .card-back .base{position:absolute;left:0;right:0;bottom:0;height:20px;background:var(--navy);display:flex;align-items:center;justify-content:flex-end;padding-right:12px;color:#fff;font-size:8.5px}

  /* Business card front */
  .card-front{left:60px;top:776px;width:360px;height:206px;background:linear-gradient(160deg,var(--navy-light),var(--navy) 55%,var(--navy-deep))}
  .card-front .brand{position:absolute;left:50%;top:50%;transform:translate(-50%,-50%)}
  .card-front .brand-name{font-size:20px}
  .card-front .watermark{left:250px;top:40px;width:80px;height:80px;background:rgba(255,255,255,.06)}

  /* Letterhead */
  .letterhead{left:610px;top:150px;width:530px;height:686px}
  .letterhead .brand{position:absolute;left:40px;top:44px}
  .letterhead .sender{position:absolute;right:40px;top:42px;text-align:right;font-size:10px;line-height:1.4}
  .letterhead .sender strong{color:var(--navy);font-weight:600;font-size:12px}
  .letterhead .rule{position:absolute;left:40px;right:40px;top:88px;height:2px;background:linear-gradient(90deg,var(--navy) 0 75%,var(--red) 75%)}
  .letterhead .watermark{left:185px;top:260px;width:160px;height:160px}
  .letterhead .footer{position:absolute;left:0;right:0;bottom:0;height:56px;background:linear-gradient(180deg,var(--navy),var(--navy-deep));color:#fff;font-size:9px;text-align:center;display:flex;flex-direction:column;justify-content:center;gap:3px}
</style>
</head>
<body>

<section class="envelope-back" aria-label="Envelope back with open flap">
  <svg class="flap" viewBox="0 0 500 82" aria-hidden="true">
    <defs>
      <linearGradient id="flapFill" x1="0" y1="0" x2="0" y2="1">
        <stop offset="0" stop-color="#0c2447"/>
        <stop offset="1" stop-color="#2f5e99"/>
      </linearGradient>
    </defs>
    <polygon points="60,0 440,0 500,82 0,82" fill="url(#flapFill)"/>
  </svg>
  <p class="flap-site">www.trclaimpro.com</p>
  <div class="pocket">
    <svg viewBox="0 0 500 150" aria-hidden="true">
      <polygon points="0,0 250,95 500,0 500,150 0,150" fill="var(--paper-shade)"/>
      <polyline points="0,0 250,95 500,0" fill="none" stroke="#d6dae0" stroke-width="1"/>
    </svg>
  </div>
</section>

<section class="sheet envelope" aria-label="Envelope front">
  <div class="watermark" aria-hidden="true"></div>
  <div class="brand"><span class="brand-mark"></span><span class="brand-name">TR Claim Advisors</span></div>
  <div class="rule"></div>
  <p class="return">58 W. Alder St. Suite 612, Smithtown, NY 11492</p>
</section>

<section class="sheet card-back" aria-label="Business card back">
  <div class="watermark" aria-hidden="true"></div>
  <div class="brand"><span class="brand-mark"></span><span class="brand-name">TR Claim Advisors</span></div>
  <div class="rule"></div>
  <div class="name-bar">
    <p class="person">Doran T. Whitcombe</p>
    <p class="title">Sr. Public Adjuster</p>
  </div>
  <div class="details">
    <p>58 W. Alder St.</p>
    <p>Suite 612</p>
    <p>Smithtown, NY 11492</p>
    <p><span class="label">Office:</span> 516.843.9075</p>
    <p><span class="label">Fax:</span> 516.843.9075</p>
    <p><span class="label">Cell:</span> 516.843.9829</p>
    <p>doran@trclaimpro.com</p>
  </div>
  <div class="base">www.trclaimpro.com</div>
</section>

<section class="sheet card-front" aria-label="Business card front">
  <div class="watermark" aria-hidden="true"></div>
  <div class="brand on-dark"><span class="brand-mark"></span><span class="brand-name">TR Claim Advisors</span></div>
</section>

<section class="sheet letterhead" aria-label="Letterhead">
  <div class="watermark" aria-hidden="true"></div>
  <div class="brand"><span class="brand-mark"></span><span class="brand-name">TR Claim Advisors</span></div>
  <div class="sender">
    <strong>Doran T. Whitcombe</strong><br>Sr. Public Adjuster
  </div>
  <div class="rule"></div>
  <div class="footer">
    <p>58 W. Alder St. Suite 612, Smithtown, NY 11492</p>
    <p>516.843.9075 &nbsp;|&nbsp; doran@trclaimpro.com &nbsp;|&nbsp; www.trclaimpro.com</p>
  </div>
</section>

</body>
</html>
```